Business Card Design for Bright Harbor Paths, LLC

Using my logo created by Pixel Tide, please create a 2 sided business card that will have an lasting affect on my potential clients. I would like my name (Dennis R. Holt, MBA), title (Owner), phone numbers or Contact Info: 312 555-0148 and 312 555-0193. Website: http://www.brantleyfordcircle.com/dennisholt/. On the back side of the card use the Certified Brantley Ford Seal that I attached. You can decide to put either my company name or what I do or nothing at all.

Target Market(s)

Large to small business, owners, Information Technology Leaders, Government and City Leaders.

Industry/Entity Type

Business

Contact Information for Business Card

It is in the description. I would like my name (Dennis R. Holt, MBA), title (Owner), phone numbers or Contact Info: 312 555-0148 and 312 555-0193. Website: http://www.brantleyfordcircle.com/dennisholt/. On the back side of the card use the Certified Brantley Ford Seal that I attached.

Colors

Designer to choose colors to be used in the design.

Requirements
Must have
• Do not change the seal that is on the back or it's color.

```html
<!DOCTYPE html>
<html lang="en">
<head>
<meta charset="utf-8">
<title>Bright Harbor Paths, LLC — Business Card</title>
<link rel="stylesheet" href="https://fonts.googleapis.com/css2?family=Arimo:wght@400;700&display=swap">
<style>
  :root {
    --page-bg: #d8d5d1;
    --card-bg: #0f0f10;
    --card-edge: #1c1c1e;
    --ink-white: #f4f4f4;
    --ink-soft: #c9c9c9;
    --ink-faint: #3a3a3c;
    --url-grey: #8d8d8f;
    --seal-gold: #c9a23a;
    --seal-gold-light: #e6c55e;
    --divider: #8a8a8a;
  }
  * { margin: 0; padding: 0; box-sizing: border-box; }
  html, body {
    width: 1200px; height: 864px; overflow: hidden;
    background: var(--page-bg);
    font-family: "Arimo", Arial, sans-serif;
  }
  .sheet { position: relative; width: 1200px; height: 864px; }
  .card {
    position: absolute; left: 250px; width: 700px; height: 400px;
    background: var(--card-bg);
    border: 1px solid var(--card-edge);
    border-radius: 4px;
    box-shadow: 0 6px 18px rgba(0,0,0,0.25);
    overflow: hidden;
  }
  .card--back { top: 20px; }
  .card--front { top: 444px; }

  /* back side */
  .back__brand {
    position: absolute; left: 90px; top: 140px; width: 330px;
    font-size: 24px; font-weight: 700; color: var(--ink-faint);
    text-align: center; white-space: nowrap;
  }
  .back__seal {
    position: absolute; right: 80px; top: 90px;
    width: 120px; height: 120px;
  }
  .back__url {
    position: absolute; left: 70px; top: 262px;
    font-size: 15px; color: var(--url-grey); white-space: nowrap;
  }

  /* front side */
  .front__brand {
    position: absolute; left: 30px; top: 0; width: 340px; height: 400px;
    display: flex; align-items: center; justify-content: center;
  }
  .front__brand-name {
    font-size: 26px; font-weight: 400; color: var(--ink-white);
    text-align: center; white-space: nowrap;
  }
  .front__divider {
    position: absolute; left: 395px; top: 120px;
    width: 1px; height: 170px; background: var(--divider);
  }
  .front__contact {
    position: absolute; left: 425px; top: 142px; width: 255px;
    color: var(--ink-white);
  }
  .contact__name { font-size: 23px; font-weight: 700; white-space: nowrap; }
  .contact__title { font-size: 16px; color: var(--ink-soft); margin-top: 4px; }
  .contact__phones { list-style: none; margin-top: 20px; }
  .contact__phone {
    display: flex; align-items: center; gap: 10px;
    font-size: 18px; line-height: 1.45; white-space: nowrap;
  }
  .contact__icon { width: 17px; height: 17px; fill: var(--ink-white); flex: none; }
</style>
</head>
<body>
<main class="sheet">

  <section class="card card--back" aria-label="Card back">
    <div class="back__brand">Bright Harbor Paths, LLC</div>
    <svg class="back__seal" viewBox="0 0 120 120" role="img" aria-label="Certified member seal">
      <circle cx="60" cy="60" r="58" fill="var(--seal-gold)"/>
      <circle cx="60" cy="60" r="46" fill="none" stroke="var(--seal-gold-light)" stroke-width="2"/>
    </svg>
    <p class="back__url">http://www.brantleyfordcircle.com/dennisholt/</p>
  </section>

  <section class="card card--front" aria-label="Card front">
    <div class="front__brand">
      <span class="front__brand-name">Bright Harbor Paths, LLC</span>
    </div>
    <div class="front__divider"></div>
    <div class="front__contact">
      <h1 class="contact__name">Dennis R. Holt, MBA</h1>
      <p class="contact__title">Owner</p>
      <ul class="contact__phones">
        <li class="contact__phone">
          <svg class="contact__icon" viewBox="0 0 24 24" aria-hidden="true"><path d="M6.6 10.8a15.1 15.1 0 0 0 6.6 6.6l2.2-2.2a1 1 0 0 1 1-.25 11.4 11.4 0 0 0 3.6.57 1 1 0 0 1 1 1V20a1 1 0 0 1-1 1A17 17 0 0 1 3 4a1 1 0 0 1 1-1h3.5a1 1 0 0 1 1 1c0 1.25.2 2.45.57 3.57a1 1 0 0 1-.25 1z"/></svg>
          312 555-0148
        </li>
        <li class="contact__phone">
          <svg class="contact__icon" viewBox="0 0 24 24" aria-hidden="true"><path d="M6.6 10.8a15.1 15.1 0 0 0 6.6 6.6l2.2-2.2a1 1 0 0 1 1-.25 11.4 11.4 0 0 0 3.6.57 1 1 0 0 1 1 1V20a1 1 0 0 1-1 1A17 17 0 0 1 3 4a1 1 0 0 1 1-1h3.5a1 1 0 0 1 1 1c0 1.25.2 2.45.57 3.57a1 1 0 0 1-.25 1z"/></svg>
          312 555-0193.
        </li>
      </ul>
    </div>
  </section>

</main>
</body>
</html>
```